LA Billboard Project for Brisk Lending

We are running three different billboards around LA, and we need someone to take the mock-ups I've created and bring this campaign to life. Whatever wording is on the mock-ups should stay the same in the ads you create, but feel free to get creative with layout and style. I've attached our mock-ups, our style guide, our logo, and the necessary specs for the billboards. If you have any questions, feel free to reach out!

```html
<!DOCTYPE html>
<html lang="en">
<head>
<meta charset="utf-8">
<title>Brisk Lending – LA Billboards</title>
<link rel="stylesheet" href="https://fonts.googleapis.com/css2?family=Barlow:wght@500;600&display=swap">
<style>
  :root {
    --page: #f9f9f9;
    --navy: #0b2442;
    --cyan: #3bc3d6;
    --yellow: #fde004;
    --white: #ffffff;
    --chevron: #9a9a9a;
    --art-flag: #d9a640;
    --art-plaza: #b5a49a;
    --art-road: #8f7070;
  }
  * { margin: 0; padding: 0; box-sizing: border-box; }
  html, body { width: 1200px; height: 2256px; overflow: hidden; }
  body {
    background: var(--page);
    position: relative;
    font-family: "Barlow", Arial, sans-serif;
  }
  .billboard {
    position: absolute;
    left: 116px;
    width: 967px;
    height: 437px;
    background: var(--navy);
    box-shadow: 0 40px 40px -22px rgba(0,0,0,0.55);
    overflow: hidden;
  }
  .billboard--pride { top: 155px; }
  .billboard--strategy { top: 908px; }
  .billboard--traffic { top: 1659px; }

  .headline {
    position: absolute;
    left: 54px;
    color: var(--white);
    font-weight: 500;
    font-size: 34px;
    line-height: 41px;
    letter-spacing: 0.12em;
    text-transform: uppercase;
  }
  .billboard--pride .headline { top: 48px; }
  .billboard--strategy .headline { top: 142px; }
  .billboard--traffic .headline { top: 82px; }

  .highlight {
    background: var(--cyan);
    color: var(--navy);
    padding: 0 4px;
  }
  .callout {
    position: absolute;
    left: 45px;
    top: 162px;
    width: 437px;
    height: 92px;
    background: var(--cyan);
    color: var(--navy);
    font-weight: 500;
    font-size: 34px;
    line-height: 41px;
    letter-spacing: 0.12em;
    padding: 5px 0 0 9px;
    text-transform: uppercase;
  }
  .url-band {
    position: absolute;
    left: 0;
    width: 496px;
    height: 54px;
    background: var(--yellow);
    color: var(--navy);
    font-weight: 600;
    font-size: 35px;
    line-height: 54px;
    letter-spacing: 0.03em;
    white-space: nowrap;
  }
  .billboard--pride .url-band { top: 329px; padding-left: 54px; }
  .billboard--strategy .url-band { top: 327px; text-align: center; padding-left: 20px; }
  .billboard--traffic .url-band { top: 329px; text-align: center; padding-left: 20px; }

  .brand {
    position: absolute;
    left: 664px;
    top: 320px;
    display: flex;
    align-items: center;
    gap: 10px;
    color: var(--cyan);
    font-weight: 600;
    font-size: 30px;
    letter-spacing: 0.02em;
    white-space: nowrap;
  }
  .brand__mark { width: 14px; height: 14px; background: var(--yellow); }

  .artwork { position: absolute; border-radius: 4px; }
  .artwork--flag  { left: 614px; top: 55px; width: 238px; height: 193px; background: var(--art-flag); }
  .artwork--plaza { left: 614px; top: 60px; width: 234px; height: 220px; background: var(--art-plaza); }
  .artwork--road  { left: 588px; top: 60px; width: 289px; height: 195px; background: var(--art-road); }

  .divider { position: absolute; left: 585px; width: 30px; height: 16px; }
  .divider--one { top: 670px; }
  .divider--two { top: 1422px; }
  .divider--end { top: 2186px; height: 2px; background: var(--chevron); }
</style>
</head>
<body>

  <section class="billboard billboard--pride">
    <p class="headline">Did you know that<br>same-sex borrowers<br>are <span class="highlight">73%</span> more likely<br>to be denied<br>when applying for<br>a mortgage loan?</p>
    <div class="url-band">BRISKLENDING.COM/LGBT</div>
    <div class="artwork artwork--flag" role="img" aria-label="Illustration: waving rainbow pride flag"></div>
    <div class="brand"><span class="brand__mark"></span>Brisk Lending</div>
  </section>

  <svg class="divider divider--one" viewBox="0 0 30 16" aria-hidden="true"><polyline points="1,2 15,14 29,2" fill="none" stroke="var(--chevron)" stroke-width="1.6"/></svg>

  <section class="billboard billboard--strategy">
    <p class="headline">What’s your<br>mortgage strategy?</p>
    <div class="url-band">BRISKREFI.COM</div>
    <div class="artwork artwork--plaza" role="img" aria-label="Illustration: isometric city block with an apartment building, trees, benches and street lamps"></div>
    <div class="brand"><span class="brand__mark"></span>Brisk Lending</div>
  </section>

  <svg class="divider divider--two" viewBox="0 0 30 16" aria-hidden="true"><polyline points="1,2 15,14 29,2" fill="none" stroke="var(--chevron)" stroke-width="1.6"/></svg>

  <section class="billboard billboard--traffic">
    <p class="headline">Traffic is a mess.</p>
    <p class="callout">Your mortgage<br>doesn’t have to be.</p>
    <div class="url-band">BRISKAPPLY.COM</div>
    <div class="artwork artwork--road" role="img" aria-label="Illustration: isometric road section with three small cars"></div>
    <div class="brand"><span class="brand__mark"></span>Brisk Lending</div>
  </section>

  <div class="divider divider--end"></div>

</body>
</html>
```